Bellwaterhomes.com requires a powerful call to action landing page to attract sellers in Ontario

We are a new Toronto based real estate company, starting an advertisement campaign online to get sellers and buyers.
This will be the landing page for them to view and submit their contact information.

This page should feature:
- Our Previous Sold Listings (which I will provide via email) Including high quality pictures
- An "explainer" video included on the page
- Fast to load, with high quality imaging
- A section of this page should include a contact/submit form for potential clients
- Company contact information
- Bottom of page will include testimonial videos from past clients

I would like the page to be very clean and minimalistic, I will be sending you a 2-300 word sales copy to be placed on the site.
Our design should reflect our logo colours, which will also be attached.

Our page should be elegant, luxurious looking and stand out from the competition.
Updates

Target Market(s)

Looking to target, people all over the Ontario looking to sell their homes.

Industry/Entity Type

Real Estate

Number of Pages Required

1 page

Requirements
Must have
• Header/cover to feature slide show of previous sold listings (see link below for listings) with high quality images (click virtual tour for each listing HQ images) and few details such as; rooms, bathrooms, city. Please also add a strong emphasis on listing detail such as; Days on market(DOM), List price and sold price, calculated over asking value in ($) (sold price minus list price)
• http://v3.quillardlistings.net/Live/Pages/Public/Link.aspx?Key=c391e48d33515ebf9968f35b4801cb85&App=QRLB

```html
<!DOCTYPE html>
<html lang="en">
<head>
<meta charset="utf-8">
<title>Bellwater Homes</title>
<link href="https://fonts.googleapis.com/css2?family=Open+Sans:wght@300;400;600;700&display=swap" rel="stylesheet">
<style>
:root{
  --red:#e3131b;
  --ink:#222;
  --text:#555;
  --muted:#888;
  --light:#f3f3f3;
  --line:#e2e2e2;
  --dark:#2a2a2a;
  --darker:#1e1e1e;
  --white:#fff;
}
*{box-sizing:border-box;margin:0;padding:0}
html,body{width:674px;height:1200px;overflow:hidden}
body{font-family:'Open Sans',sans-serif;color:var(--text);background:var(--white);position:relative}
.wrap{position:absolute;left:55px;right:55px}
.topbar{position:absolute;top:0;left:0;width:674px;height:19px;background:#f7f7f7;border-bottom:1px solid var(--line);font-size:6.5px;color:var(--text)}
.topbar .contact{position:absolute;left:55px;top:5px;display:flex;gap:16px;align-items:center}
.topbar .contact span{display:flex;align-items:center;gap:3px}
.topbar .social{position:absolute;right:55px;top:5px;display:flex;gap:8px;align-items:center}
.dot{width:7px;height:7px;border-radius:50%;background:var(--red);display:inline-block}
.header{position:absolute;top:19px;left:0;width:674px;height:54px;background:var(--white)}
.brand{position:absolute;left:55px;top:16px;display:flex;align-items:center;gap:6px;font-size:15px;font-weight:600;color:var(--ink)}
.brand i{width:16px;height:16px;background:var(--red);display:inline-block}
.nav{position:absolute;right:55px;top:24px;display:flex;gap:34px;font-size:7.5px;color:var(--text)}
.hero{position:absolute;top:73px;left:0;width:674px;height:280px;background:linear-gradient(180deg,#1b2744 0%,#2b3b5c 45%,#4b3a2c 75%,#1e2230 100%)}
.hero .arrow{position:absolute;top:136px;width:16px;height:16px;border-radius:50%;background:rgba(255,255,255,.18)}
.hero h1{position:absolute;left:56px;top:188px;font-size:17px;font-weight:700;color:var(--white);letter-spacing:.2px}
.hero p{position:absolute;left:56px;top:211px;width:290px;font-size:9px;line-height:18px;color:var(--white)}
.band{position:absolute;top:353px;left:0;width:674px;height:65px;background:var(--dark)}
.band p{position:absolute;left:56px;top:15px;width:420px;font-size:9px;line-height:17px;color:#9a9a9a;font-weight:300}
.btn{background:var(--red);color:var(--white);font-weight:700;text-transform:uppercase;display:flex;align-items:center;justify-content:center;border-radius:2px}
.band .btn{position:absolute;left:492px;top:19px;width:99px;height:30px;font-size:7.5px;box-shadow:0 2px 0 #a70d12}
.welcome{position:absolute;top:418px;left:0;width:674px;height:124px;text-align:center}
.welcome h2{margin-top:35px;font-size:12px;font-weight:700;color:var(--ink)}
.welcome p{width:510px;margin:8px auto 0;font-size:6.8px;line-height:13px;color:var(--text)}
.sold{position:absolute;top:542px;left:0;width:674px;height:176px;background:var(--light);border-top:1px solid var(--line);border-bottom:1px solid var(--line)}
.section-title{font-size:10px;font-weight:700;color:var(--ink);text-transform:uppercase}
.sold .section-title{position:absolute;left:55px;top:24px}
.sold .pager{position:absolute;right:55px;top:22px;display:flex;gap:4px}
.sold .pager span{width:15px;height:15px;background:var(--white);border:1px solid var(--line);font-size:8px;color:#aaa;display:flex;align-items:center;justify-content:center}
.listings{position:absolute;left:55px;top:58px;display:flex;gap:14px}
.photo{width:130px;height:87px;box-shadow:0 4px 5px rgba(0,0,0,.2)}
.p1{background:linear-gradient(135deg,#c98a4a,#e9d6b4 60%,#7a4a2a)}
.p2{background:linear-gradient(180deg,#d9e6f1,#f1ece2 55%,#4d9cc7 85%,#6f8a4a)}
.p3{background:linear-gradient(180deg,#5c7496,#3a3f4a 55%,#c99a5a 75%,#2a2a2a)}
.p4{background:linear-gradient(180deg,#9bb0bc,#6d7f72 45%,#2b2b2b 75%,#e6e6e6)}
.explainer .section-title{position:absolute;left:55px;top:749px}
.video{position:relative}
.explainer .video{position:absolute;left:55px;top:775px;width:274px;height:183px;background:linear-gradient(180deg,#c9dbe8 0%,#9fb7c4 35%,#4f7a3c 65%,#2f4f2a 100%)}
.play{position:absolute;left:50%;top:50%;transform:translate(-50%,-50%);width:46px;height:32px;background:var(--red);border-radius:7px;display:flex;align-items:center;justify-content:center}
.contact-form .section-title{position:absolute;left:362px;top:749px}
.field{position:absolute;border:1px solid #d8d8d8;background:var(--white);font-size:6.8px;color:var(--muted);padding:5px 8px}
.form-btn{position:absolute;left:491px;top:822px;width:75px;height:23px;font-size:7px;box-shadow:0 2px 0 #a70d12}
.info .section-title{position:absolute;left:362px;top:869px}
.info .name{position:absolute;left:363px;top:895px;font-size:7px;font-weight:700;color:var(--red)}
.info .addr{position:absolute;left:363px;top:910px;font-size:6.8px;line-height:14px;color:var(--text)}
.info .lines{position:absolute;left:363px;top:946px;display:flex;gap:22px;font-size:6.8px;color:var(--text)}
.info .lines span{display:flex;align-items:center;gap:5px}
.info .logo-box{position:absolute;left:482px;top:893px;width:136px;height:45px;border:1px solid #ddd;display:flex;align-items:center;justify-content:center;gap:6px;font-size:11px;font-weight:600;color:var(--ink)}
.info .logo-box i{width:12px;height:12px;background:var(--red);display:inline-block}
.footer{position:absolute;top:990px;left:0;width:674px;height:178px;background:var(--dark)}
.footer h4{position:absolute;top:25px;font-size:7.5px;font-weight:700;color:#d0d0d0;text-transform:uppercase}
.footer .video{position:absolute;left:55px;top:47px;width:177px;height:108px;background:linear-gradient(135deg,#e8eef2,#c8d4dc 55%,#9aa8b3)}
.footer .play{width:32px;height:22px;border-radius:5px}
.footer .about{position:absolute;left:273px;top:46px;width:190px;font-size:6px;line-height:12px;color:#777}
.footer .about p+p{margin-top:10px}
.footer .more{position:absolute;left:275px;top:144px;font-size:6.3px;color:#ddd;display:flex;align-items:center;gap:5px}
.footer .more .dot{width:5px;height:5px}
.footer ul{position:absolute;left:518px;top:47px;list-style:none;font-size:6.3px;line-height:14.4px;color:#777}
.bottom{position:absolute;top:1168px;left:0;width:674px;height:32px;background:var(--darker);text-align:center;font-size:6px;color:#666;padding-top:12px}
</style>
</head>
<body>

<div class="topbar">
  <div class="contact">
    <span><svg width="7" height="7" viewBox="0 0 10 10"><path d="M2 0.5l2 2.2-1 1.2c.6 1.3 1.7 2.4 3 3l1.2-1 2.3 2-1.2 1.6C4.5 9.3.7 5.5.5 1.7z" fill="#e3131b"/></svg>(416) 555 0142</span>
    <span><svg width="7" height="6" viewBox="0 0 10 8"><rect width="10" height="8" fill="#e3131b"/><path d="M0 0l5 4 5-4" stroke="#fff" fill="none"/></svg>info@bellwaterhomes.com</span>
  </div>
  <div class="social">
    <span>Connect with our social network :</span>
    <i class="dot"></i><i class="dot"></i><i class="dot"></i><i class="dot"></i><i class="dot"></i>
  </div>
</div>

<header class="header">
  <div class="brand"><i></i>Bellwater Homes</div>
  <nav class="nav"><span>About us</span><span>Services</span><span>Property</span><span>Videos</span><span>Testimonials</span><span>Contact Us</span></nav>
</header>

<section class="hero" role="img" aria-label="Luxury home at dusk with lit windows and a reflecting pool">
  <span class="arrow" style="left:23px"></span>
  <span class="arrow" style="right:27px"></span>
  <h1>BELLWATER HOMES</h1>
  <p>We are a new Toronto based real estate company, starting an advertisement campaign online to get sellers and buyers.</p>
</section>

<section class="band">
  <p>We are a new Toronto based real estate company, starting an advertisement campaign online to get sellers and buyers.</p>
  <a class="btn">Get in touch</a>
</section>

<section class="welcome">
  <h2>WELCOME TO BELLWATER HOMES</h2>
  <p>Es simplemente el texto de relleno de las imprentas y archivos de texto. Lorem Ipsum ha sido el texto de relleno estándar de las industrias desde el año 1500, cuando un impresor desconocido usó una galería de textos y los mezcló de tal manera que logró hacer un libro de textos especimen. No sólo sobrevivió 500 años</p>
</section>

<section class="sold">
  <h3 class="section-title">Our previous sold listings</h3>
  <div class="pager"><span>‹</span><span>›</span></div>
  <div class="listings">
    <div class="photo p1" role="img" aria-label="Living room with wood panelled walls"></div>
    <div class="photo p2" role="img" aria-label="White villa with swimming pool"></div>
    <div class="photo p3" role="img" aria-label="Modern house lit at dusk"></div>
    <div class="photo p4" role="img" aria-label="Terrace lounge overlooking a lake and mountains"></div>
  </div>
</section>

<section class="explainer">
  <h3 class="section-title">Explainer</h3>
  <div class="video" role="img" aria-label="Explainer video: residential towers above green parkland">
    <span class="play"><svg width="12" height="13" viewBox="0 0 12 13"><path d="M0 0l12 6.5L0 13z" fill="#fff"/></svg></span>
  </div>
</section>

<section class="contact-form">
  <h3 class="section-title">Contact form</h3>
  <div class="field" style="left:363px;top:776px;width:121px;height:19px">Name</div>
  <div class="field" style="left:363px;top:801px;width:121px;height:19px">Email</div>
  <div class="field" style="left:363px;top:826px;width:121px;height:19px">Phone</div>
  <div class="field" style="left:491px;top:776px;width:121px;height:38px">Message</div>
  <a class="btn form-btn">Submit now</a>
</section>

<section class="info">
  <h3 class="section-title">Contact information</h3>
  <div class="name">BELLWATER HOMES</div>
  <div class="addr">120 Street name, City name,<br>Country name : 236566</div>
  <div class="lines">
    <span><svg width="8" height="8" viewBox="0 0 10 10"><path d="M2 0.5l2 2.2-1 1.2c.6 1.3 1.7 2.4 3 3l1.2-1 2.3 2-1.2 1.6C4.5 9.3.7 5.5.5 1.7z" fill="#e3131b"/></svg>(416) 555 0142</span>
    <span><svg width="8" height="6" viewBox="0 0 10 8"><rect width="10" height="8" fill="#e3131b"/><path d="M0 0l5 4 5-4" stroke="#fff" fill="none"/></svg>info@bellwaterhomes.com</span>
  </div>
  <div class="logo-box"><i></i>Bellwater Homes</div>
</section>

<footer class="footer">
  <h4 style="left:56px">Testimonial video</h4>
  <div class="video" role="img" aria-label="Testimonial video from a past client working on a laptop">
    <span class="play"><svg width="9" height="10" viewBox="0 0 12 13"><path d="M0 0l12 6.5L0 13z" fill="#fff"/></svg></span>
  </div>
  <h4 style="left:273px">About Bellwater Homes</h4>
  <div class="about">
    <p>Es simplemente el texto de relleno de las imprentas y archivos de texto. Lorem Ipsum ha sido el texto de relleno estándar de las industrias desde el año 1500, cuando un impresor desconocido usó una galería de textos y los mezcló</p>
    <p>De tal manera que logró hacer un libro de textos especimen. No sólo sobrevivió 500 años</p>
  </div>
  <div class="more">Click here for more details <i class="dot"></i></div>
  <h4 style="left:518px">Welcome</h4>
  <ul><li>Home</li><li>About us</li><li>Services</li><li>Property</li><li>Videos</li><li>Testimonials</li><li>Contact Us</li></ul>
</footer>

<div class="bottom">© 2015. Bellwater Homes. All rights reserved.</div>

</body>
</html>
```